Letterhead design for business

Looking for an attractive and professional letterhead that uses the logo that is attached below.

Target Market(s)

Potential bankruptcy clients.

Industry/Entity Type

Legal

Colors

Designer to choose colors to be used in the design.

Requirements
Must have
• Address for locations, phone number, and website address.
• Addresses are on website ferncoveadvice.example. Use following phone number (for tracking purposes): 555-013-8274

```html
<!DOCTYPE html>
<html lang="en">
<head>
<meta charset="utf-8">
<title>Fernbrook Law Group – Letterhead</title>
<link href="https://fonts.googleapis.com/css2?family=Arimo:wght@400;700&display=swap" rel="stylesheet">
<style>
  :root {
    --canvas-bg: #d8d5cf;
    --paper: #f4f5ec;
    --ink-dark: #4a4a4a;
    --ink-body: #8c8c8c;
    --rule: #555555;
  }
  * { box-sizing: border-box; margin: 0; padding: 0; }
  html, body {
    width: 1200px; height: 900px; overflow: hidden;
    background: var(--canvas-bg);
    font-family: "Arimo", Arial, sans-serif;
  }
  .letterhead {
    position: absolute; left: 266px; top: 20px;
    width: 667px; height: 860px;
    background: var(--paper);
    box-shadow: 0 2px 8px rgba(0,0,0,0.15);
  }
  .brand {
    position: absolute; left: 30px; top: 40px;
    font-size: 17px; font-weight: 700; color: var(--ink-dark);
    line-height: 1;
  }

  .contact {
    position: absolute; left: 311px; top: 22px;
    font-size: 8.5px; color: var(--ink-dark);
    display: grid; grid-template-columns: 96px auto; row-gap: 3px;
  }
  .contact dt { font-weight: 700; }
  .contact dd { font-size: 7.5px; }
  .contact .addr-first { border-bottom: 1px solid var(--rule); padding-bottom: 1px; }
  .contact .addr-label { align-self: center; grid-row: span 2; }

  .recipient {
    position: absolute; left: 49px; top: 188px;
    font-size: 11.5px; font-weight: 700; color: var(--ink-body);
  }
  .body-copy {
    position: absolute; left: 49px; top: 220px; width: 570px;
    font-size: 10px; line-height: 11.3px; color: var(--ink-body);
    text-align: justify; letter-spacing: 0.7px;
  }
  .body-copy p { margin-bottom: 22px; }
  .body-copy p.lead { text-indent: 25px; }

  .signoff {
    position: absolute; right: 50px; top: 614px;
    text-align: right; font-size: 11px; font-weight: 700; color: var(--ink-dark);
  }
  .signoff .role { font-size: 10px; margin-top: 2px; }
  .signature {
    margin-top: 8px; margin-left: auto;
    width: 80px; height: 22px;
    background: linear-gradient(90deg, #e4e5dc, #d6d7ce);
  }
</style>
</head>
<body>
  <main class="letterhead">
    <header>
      <div class="brand">Fernbrook Law Group</div>
      <dl class="contact">
        <dt class="addr-label">Address</dt>
        <dd class="addr-first">: 418 Larkspur Ave., Suite #310 Milltown, Georgia 30999</dd>
        <dd>&nbsp;&nbsp;92 Orchard Row, Pinecrest, Georgia 30998</dd>
        <dt>Phone</dt>
        <dd>: 555-013-8274</dd>
        <dt>website address</dt>
        <dd>: https://ferncoveadvice.example</dd>
      </dl>
    </header>

    <div class="recipient">JHONE DOE</div>

    <section class="body-copy">
      <p class="lead">Lorem Ipsum is simply dummy text of the printing and typesetting industry. Lorem Ipsum has been the industry's standard dummy text ever since the 1500s, when an unknown printer took a galley of type and scrambled it to make a type specimen book. It has survived not only five centuries, but also the leap into electronic typesetting, remaining essentially unchanged. It was popularised in the 1960s with the release of Letraset sheets containing Lorem Ipsum passages, and more recently with desktop publishing software like Aldus PageMaker including versions of Lorem Ipsum.</p>
      <p>Lorem Ipsum is simply dummy text of the printing and typesetting industry. Lorem Ipsum has been the industry's standard dummy text ever since the 1500s, when an unknown printer took a galley of type and scrambled it to make a type specimen book. It has survived not only five centuries, but also the leap into electronic typesetting, remaining essentially unchanged. It was popularised in the 1960s with the release of Letraset sheets containing Lorem Ipsum passages, and more recently with desktop publishing software like Aldus PageMaker including versions of Lorem Ipsum.Lorem Ipsum is simply dummy text of the printing and typesetting industry. Lorem Ipsum has been the industry's standard dummy text ever since the 1of Letraset sheets containing Lorem Ipsum passages, and more recently with desktop publishing software like Aldus PageMaker including versions of Lorem Ipsum.Lorem Ipsum is simply dummy text of the printing and typesetting industry. Lorem Ipsum has been the industry's standard dummy text ever since the 1</p>
      <p>Lorem Ipsum is simply dummy text of the printing and typesetting industry. Lorem Ipsum has been the industry's standard dummy text ever since the 1500s, when an unknown printer took a galley of type and scrambled it to make a type specimen book. It has survived not only five centuries, but also the leap into electronic typesetting, remaining essentially unchanged. It was popularised in the 1960s with the release of Letraset</p>
      <p>Lorem Ipsum is simply dummy text of the printing and typesetting industry. Lorem Ipsum has been the industry's standard dummy text ever since the 1500s, when an unknown printer took a galley of type and scrambled it to make a type specimen book. It has survived not</p>
    </section>

    <footer class="signoff">
      <div>JHONE DOE</div>
      <div class="role">Owner</div>
      <div class="signature" role="img" aria-label="Handwritten signature"></div>
    </footer>
  </main>
</body>
</html>
```